Packaging Design: Logo/Bottle Design for New Botanical Cocktail Brand

We are a new start up, looking to create a new line of Ready to drink Cocktails. The brand name is Verdelle Garden Cocktails, infused with fruit, herb, and floral botanicals grown on our farm in New Hampshire. Flavors will include: Herb flavored with cilantro, Berry- flavored with Alpine Strawberry, Citrus flavored with lemon Verbena & lemon balm, Pear flavored with Bartlett pear, Cucumber & Mint. We need a logo and a label design. There are 2 possible bottles to choose from.

Designer has complete freedom with everything! From fonts and colors to bottle caps and closures. Please view the pinterest link for inspirational bottle designs. https://www.pinboardly.example/kestrawynn/garden-drinks/

Target Market(s)

Female 21 to 48 years old. College educated and professional. The type of person that has a passion for a cause and eats and shops local. People that respect an artisan quality product, hand made by a master craftsman.

Industry/Entity Type

Floral

Requirements
Must have
• Clear Bottle, see options attached. You may also choose your own BUT WE MUST SEE THE LOGO AND IMAGERY ON A BOTTLE
• Logo Design: "Verdelle Garden Cocktails"
• Label: We can have front and back, or one continuous label. We are open to painted designs.
• The label must contain the following text in quotes:
• Product Name: " Verdelle Garden Cocktails "
• "15% Alc. by Vol. (30 proof)"
• "750 mL"
• "Handcrafted and Bottled by Harrow Creek Orchard Farm and Distillery
• Winchester, NH-USA"
• The following Text must be in all caps and 3mm in height:
• "Government Warning: (1) According to the Surgeon General, women should not drink alcoholic beverages during pregnancy because of the risk of birth defects. (2) Consumption of alcoholic beverages impairs your ability to drive a car or operate machinery and may cause health problems."
• Must be a space for a bar code: .75 in height by 1.25 in length.
• “www.harrowcreekorchard.example”
• Must Have the following Statement:
• Infused with fruit, herb, and floral botanicals and sweetened with stevia. Serve cold over ice.
Nice to have
• Antique or vintage botanical illustrations
• https://www.pinboardly.example/kestrawynn/garden-drinks/
• check out the board for inspiration.
• Think artisanal small batch spirits that are ready to drink out of the bottle. Refreshing flavors just pour over ice and add herb leaves.
• You can use images by doing a search here.
• http://archive.plantrecords.example/search.xhtml?start=0&collectionFacet=Orchard+Fruit+Painting+Set

```html
<!DOCTYPE html>
<html lang="en">
<head>
<meta charset="utf-8">
<title>Verdelle Garden Cocktails – Labels</title>
<link href="https://fonts.googleapis.com/css2?family=Oswald:wght@400;500&family=Pinyon+Script&family=Cormorant+Garamond:ital,wght@1,500&display=swap" rel="stylesheet">
<style>
  :root {
    --page: #ffffff;
    --cream: #fbf8ea;
    --parchment: #efe3c8;
    --citrus-ink: #8b7b63;
    --citrus-band: #d4e83a;
    --citrus-leaf: #a9bb98;
    --citrus-fruit: #dcd8a4;
    --berry-ink: #6f7189;
    --berry-band: #a9a9c4;
    --berry-fruit: #7483ad;
    --berry-leaf: #93a891;
    --band-ink: #2b2b2b;
  }
  * { box-sizing: border-box; margin: 0; padding: 0; }
  html, body { width: 1200px; height: 1000px; overflow: hidden; background: var(--page); }
  .canvas { position: relative; width: 1200px; height: 1000px; }

  .neck-band {
    position: absolute; top: 232px; width: 92px; height: 48px;
    background: var(--band);
    display: flex; align-items: center; justify-content: center;
    font-family: "Oswald", sans-serif; font-weight: 500; font-size: 18px;
    letter-spacing: 0.3px; color: var(--band-ink);
  }
  .neck-band--citrus { left: 384px; --band: var(--citrus-band); }
  .neck-band--blueberry { left: 730px; --band: var(--berry-band); }

  .label { position: absolute; top: 355px; width: 184px; height: 535px; overflow: hidden; }
  .label--citrus { left: 331px; --ink: var(--citrus-ink); }
  .label--blueberry { left: 687px; --ink: var(--berry-ink); }

  .label__art { position: absolute; inset: 0; }
  .label--citrus .label__art {
    background:
      radial-gradient(circle at 80% 22%, var(--citrus-fruit) 0 14%, transparent 15%),
      radial-gradient(circle at 88% 58%, var(--citrus-fruit) 0 10%, transparent 11%),
      radial-gradient(circle at 15% 88%, var(--citrus-fruit) 0 12%, transparent 13%),
      radial-gradient(ellipse at 8% 40%, var(--citrus-leaf) 0 10%, transparent 16%),
      radial-gradient(ellipse at 92% 78%, var(--citrus-leaf) 0 9%, transparent 15%),
      linear-gradient(180deg, #f1e6cc, var(--parchment));
  }
  .label--blueberry .label__art {
    background:
      radial-gradient(circle at 90% 26%, var(--berry-fruit) 0 8%, transparent 9%),
      radial-gradient(circle at 92% 80%, var(--berry-fruit) 0 7%, transparent 8%),
      radial-gradient(circle at 10% 48%, var(--berry-fruit) 0 8%, transparent 9%),
      radial-gradient(circle at 22% 96%, var(--berry-fruit) 0 7%, transparent 8%),
      radial-gradient(ellipse at 10% 10%, var(--berry-leaf) 0 8%, transparent 14%),
      radial-gradient(ellipse at 90% 60%, var(--berry-leaf) 0 8%, transparent 14%),
      linear-gradient(180deg, #eee4cd, var(--parchment));
  }

  .brand {
    position: absolute; left: 40px; top: 33px; width: 113px; height: 108px;
    background: var(--cream); color: var(--ink);
    display: flex; align-items: center; justify-content: center;
    padding: 0 10px; text-align: center;
    font-family: "Oswald", sans-serif; font-weight: 500; font-size: 17px;
    line-height: 1.2; text-transform: uppercase; letter-spacing: 0.5px;
  }

  .info {
    position: absolute; left: 38px; top: 170px; width: 116px; height: 340px;
    background: var(--cream); color: var(--ink); text-align: center;
    padding: 30px 8px 0;
  }
  .info__statement { font-family: "Pinyon Script", cursive; font-size: 13px; line-height: 1.5; }
  .info__serve { font-family: "Pinyon Script", cursive; font-size: 13px; margin-top: 4px; }
  .info__flavor {
    font-family: "Cormorant Garamond", serif; font-style: italic; font-weight: 500;
    font-variant: small-caps; font-size: 24px; line-height: 1; margin-top: 42px;
  }
  .label--blueberry .info__flavor { font-size: 18px; }
  .info__notes { font-family: "Oswald", sans-serif; font-size: 10.5px; line-height: 1.35; text-transform: uppercase; margin-top: 4px; }
  .info__legal { position: absolute; left: 0; right: 0; bottom: 20px; font-family: "Oswald", sans-serif; }
  .info__abv { font-size: 9px; }
  .info__volume { font-size: 11px; font-weight: 500; margin-top: 3px; }
</style>
</head>
<body>
<main class="canvas">
  <div class="neck-band neck-band--citrus">CITRUS</div>
  <section class="label label--citrus">
    <div class="label__art" role="img" aria-label="Vintage botanical illustration of citrus fruit, blossoms and leaves"></div>
    <div class="brand">Verdelle Garden Cocktails</div>
    <div class="info">
      <p class="info__statement">Infused with fruit, herb, and floral botanicals and sweetened with stevia.</p>
      <p class="info__serve">Serve cold over ice.</p>
      <p class="info__flavor">Citrus</p>
      <p class="info__notes">Flavored with<br>lemon verbena &amp;<br>lemon balm</p>
      <div class="info__legal">
        <p class="info__abv">15% Alc. by Vol. (30 proof)</p>
        <p class="info__volume">750 mL</p>
      </div>
    </div>
  </section>

  <div class="neck-band neck-band--blueberry">BLUEBERRY</div>
  <section class="label label--blueberry">
    <div class="label__art" role="img" aria-label="Vintage botanical illustration of blueberries, lavender sprigs and fern leaves"></div>
    <div class="brand">Verdelle Garden Cocktails</div>
    <div class="info">
      <p class="info__statement">Infused with fruit, herb, and floral botanicals and sweetened with stevia.</p>
      <p class="info__serve">Serve cold over ice.</p>
      <p class="info__flavor">Blueberries</p>
      <p class="info__notes">Flavored with<br>lavender</p>
      <div class="info__legal">
        <p class="info__abv">15% Alc. by Vol. (30 proof)</p>
        <p class="info__volume">750 mL</p>
      </div>
    </div>
  </section>
</main>
</body>
</html>
```